Halden Insurance Enclosed Trailer wrap

I need a design to wrap an enclosed trailer. Use our logo.
We are an insurance company. We specialize in Farm, Commercial, Auto, Home and Health insurance.
We want it to look classy and professional. Easy to read but stand out. Use pictures of a farm, home, and auto .
I will attach a link of the enclosed trailer and the measurements.
Trailer Brand is Korvex
model is kt482rb
https://www.pindlertrailerhub.example/2020-korvex-kt482rb-enclosed-cargo-trailer-7q2j%7CWTa.html
I would like a design for all sides, front peak, and rear door.
Use our logo which is attached. Our colors are royal blue, white, gray but other colors are welcome for the design.

https://www.gearlotmarket.example/Trailers/listing/2020-Korvex-KT482RB-7390158264

Industry/Entity Type

Insurance Agency

Font styles to use
Serif

Colors
0655a3
3277b5
ffffff
cedeed

Requirements
Must have
• Pictures of farm - use a bright color photo of farm, combine, silo, haybales
• home -possibly add a photo of a home and auto if room permits
• Creatively arranged photos to attract attention.
• Our Hi logo and Halden Insurance attached
• Must stand out and be professional .....
• phone number 605-218-4073
• web address is halden-insurance.example
Should not have
• Nothing boring and neutral colors

```html
<!DOCTYPE html>
<html lang="en">
<head>
<meta charset="utf-8">
<title>Halden Insurance – Enclosed Trailer Wrap</title>
<link href="https://fonts.googleapis.com/css2?family=Poppins:ital,wght@0,600;1,400;1,600;1,700&display=swap" rel="stylesheet">
<style>
  :root{
    --navy:#1c2f78;
    --navy-deep:#17286a;
    --slate:#3a434c;
    --slate-dark:#2f373f;
    --mist:#d4d9df;
    --white:#ffffff;
    --canvas:#eef0f3;
  }
  *{box-sizing:border-box;margin:0;padding:0}
  html,body{width:1200px;height:1200px;overflow:hidden;background:var(--canvas)}
  body{position:relative;font-family:"Poppins",sans-serif;color:var(--white)}

  .panel{position:absolute;overflow:hidden}
  .panel svg.backdrop{position:absolute;inset:0;width:100%;height:100%}

  /* brand lockup: plain circle + name, one colour, one weight */
  .brand{position:absolute;display:flex;flex-direction:column;align-items:center;text-align:center}
  .brand-dot{display:block;border-radius:50%;background:currentColor}
  .brand-name{display:block;font-family:"Poppins",sans-serif;font-weight:600;font-style:normal;line-height:1.1;margin-top:20px}

  .specialties h3{font-style:italic;font-weight:700;line-height:1}
  .specialties ul{list-style:none}
  .specialties li{font-style:italic;font-weight:400;display:flex;align-items:center;gap:6px;line-height:1.3}
  .specialties li svg{flex:none}
  .phone{font-style:italic;font-weight:700;letter-spacing:.01em;line-height:1}
  .web{font-style:italic;font-weight:700;line-height:1}

  /* side wall */
  .side{left:20px;top:20px;width:1160px;height:470px;background:var(--mist)}
  .side .brand{left:420px;top:80px;width:320px;color:var(--navy)}
  .side .brand-dot{width:110px;height:110px}
  .side .brand-name{font-size:48px}
  .side .specialties{position:absolute;left:800px;top:60px}
  .side .specialties h3{font-size:30px;margin-bottom:6px}
  .side .specialties li{font-size:17px}
  .side .phone{position:absolute;left:790px;top:292px;font-size:44px}
  .side .web{position:absolute;left:792px;top:344px;font-size:25px}
  .side .social{position:absolute;left:248px;top:424px;font-size:14px;font-weight:600;font-style:italic}

  /* front peak */
  .front{left:20px;top:510px;width:560px;height:670px;background:var(--navy)}
  .front .tagline{position:absolute;left:40px;top:90px;width:460px;transform:rotate(-12deg);font-style:italic;font-weight:700;font-size:46px;line-height:1.1;text-align:center}
  .front .brand{left:110px;top:290px;width:340px;color:var(--white)}
  .front .brand-dot{width:100px;height:100px}
  .front .brand-name{font-size:52px}
  .front .phone-box{position:absolute;left:55px;top:560px;width:450px;height:70px;border:3px solid var(--white);border-radius:10px;transform:rotate(-6deg);display:flex;align-items:center;justify-content:center}
  .front .phone{font-size:44px}
  .front .badge{position:absolute;right:40px;top:40px;width:70px;height:28px;border-radius:14px;background:var(--navy-deep);border:2px solid #2a3f8c}

  /* rear door */
  .rear{left:600px;top:510px;width:580px;height:670px;background:var(--slate)}
  .rear .brand{left:240px;top:80px;width:310px;color:var(--mist)}
  .rear .brand-dot{width:100px;height:100px}
  .rear .brand-name{font-size:46px}
  .rear .specialties{position:absolute;left:26px;top:352px;width:540px}
  .rear .specialties h3{font-size:28px;margin-bottom:6px}
  .rear .specialties .cols{display:flex;gap:18px}
  .rear .specialties ul{width:260px}
  .rear .specialties ul.right{padding-top:14px}
  .rear .specialties li{font-size:15px;line-height:1.2}
  .rear .phone{position:absolute;left:0;width:100%;top:500px;text-align:center;font-size:50px;color:var(--mist)}
  .rear .web-band{position:absolute;left:0;right:0;bottom:0;height:100px;background:var(--navy);display:flex;align-items:center;justify-content:center}
  .rear .web{font-size:28px}
  .rear .badge{position:absolute;right:40px;top:30px;width:70px;height:26px;border-radius:13px;background:var(--slate-dark);border:2px solid #4a545e}
</style>
</head>
<body>

<section class="panel side">
  <svg class="backdrop" viewBox="0 0 1160 470" preserveAspectRatio="none">
    <defs>
      <linearGradient id="houseTone" x1="0" y1="0" x2="1" y2="1"><stop offset="0" stop-color="#5d6d8a"/><stop offset="1" stop-color="#7fa063"/></linearGradient>
      <linearGradient id="farmTone" x1="0" y1="0" x2="0" y2="1"><stop offset="0" stop-color="#6fa8e0"/><stop offset=".55" stop-color="#c2553b"/><stop offset="1" stop-color="#5e8a2e"/></linearGradient>
      <linearGradient id="careTone" x1="0" y1="0" x2="1" y2="1"><stop offset="0" stop-color="#e9ddd0"/><stop offset="1" stop-color="#b9c3cf"/></linearGradient>
      <linearGradient id="workTone" x1="0" y1="0" x2="1" y2="1"><stop offset="0" stop-color="#c9c2b6"/><stop offset="1" stop-color="#d9b43c"/></linearGradient>
      <linearGradient id="handsTone" x1="0" y1="0" x2="1" y2="0"><stop offset="0" stop-color="#b3bcc7"/><stop offset="1" stop-color="#d4d9df"/></linearGradient>
    </defs>
    <rect x="300" y="20" width="420" height="370" fill="url(#handsTone)" role="img" aria-label="Protective hands sheltering insurance icons"/>
    <rect x="0" y="0" width="800" height="22" fill="var(--slate)"/>
    <rect x="0" y="392" width="800" height="78" fill="var(--slate)"/>
    <polygon points="790,0 1160,0 1160,470 640,470 640,392 790,392" fill="var(--navy)"/>
    <polygon points="1040,0 1160,0 1160,210" fill="var(--slate)"/>
    <polygon points="0,0 230,0 380,160 300,240 0,240" fill="var(--navy)"/>
    <polygon points="40,10 220,10 360,160 300,220 150,220 40,110" fill="url(#houseTone)" stroke="var(--navy)" stroke-width="8" role="img" aria-label="Photo of a family home with front lawn"/>
    <polygon points="0,100 50,100 130,240 0,240" fill="url(#farmTone)" stroke="var(--navy)" stroke-width="8" role="img" aria-label="Photo of a red barn and crop fields"/>
    <polygon points="150,230 310,230 380,320 340,380 200,380 150,300" fill="url(#careTone)" stroke="var(--navy)" stroke-width="8" role="img" aria-label="Photo of a caregiver with an older woman"/>
    <polygon points="0,250 140,250 230,380 220,470 0,470" fill="url(#workTone)" stroke="var(--navy)" stroke-width="8" role="img" aria-label="Photo of an injured worker with a hard hat"/>
  </svg>

  <div class="brand">
    <span class="brand-dot"></span>
    <span class="brand-name">Halden<br>Insurance</span>
  </div>

  <div class="specialties">
    <h3>We specialize</h3>
    <ul>
      <li><svg width="10" height="10" viewBox="0 0 10 10"><path d="M1 5l3 3 5-7" stroke="#fff" stroke-width="2" fill="none"/></svg>Auto Insurance</li>
      <li><svg width="10" height="10" viewBox="0 0 10 10"><path d="M1 5l3 3 5-7" stroke="#fff" stroke-width="2" fill="none"/></svg>Home Insurance</li>
      <li><svg width="10" height="10" viewBox="0 0 10 10"><path d="M1 5l3 3 5-7" stroke="#fff" stroke-width="2" fill="none"/></svg>Commercial Insurance</li>
      <li><svg width="10" height="10" viewBox="0 0 10 10"><path d="M1 5l3 3 5-7" stroke="#fff" stroke-width="2" fill="none"/></svg>Life Insurance</li>
      <li><svg width="10" height="10" viewBox="0 0 10 10"><path d="M1 5l3 3 5-7" stroke="#fff" stroke-width="2" fill="none"/></svg>Health Insurance</li>
      <li><svg width="10" height="10" viewBox="0 0 10 10"><path d="M1 5l3 3 5-7" stroke="#fff" stroke-width="2" fill="none"/></svg>Farm Insurance</li>
      <li><svg width="10" height="10" viewBox="0 0 10 10"><path d="M1 5l3 3 5-7" stroke="#fff" stroke-width="2" fill="none"/></svg>Medicare Supplemental Insurance</li>
    </ul>
  </div>
  <div class="phone">605-218-4073</div>
  <div class="web">halden-insurance.example</div>
  <div class="social">@halden-insurance.example</div>
</section>

<section class="panel front">
  <div class="badge"></div>
  <div class="tagline">The best<br>choice for you</div>
  <div class="brand">
    <span class="brand-dot"></span>
    <span class="brand-name">Halden<br>Insurance</span>
  </div>
  <div class="phone-box"><span class="phone">605-218-4073</span></div>
</section>

<section class="panel rear">
  <svg class="backdrop" viewBox="0 0 580 670" preserveAspectRatio="none">
    <polygon points="0,0 170,0 260,150 0,300" fill="var(--navy)"/>
  </svg>
  <div class="badge"></div>
  <div class="brand">
    <span class="brand-dot"></span>
    <span class="brand-name">Halden<br>Insurance</span>
  </div>
  <div class="specialties">
    <h3>We specialize</h3>
    <div class="cols">
      <ul>
        <li><svg width="9" height="9" viewBox="0 0 10 10"><path d="M1 5l3 3 5-7" stroke="#fff" stroke-width="2" fill="none"/></svg>Auto Insurance</li>
        <li><svg width="9" height="9" viewBox="0 0 10 10"><path d="M1 5l3 3 5-7" stroke="#fff" stroke-width="2" fill="none"/></svg>Home Insurance</li>
        <li><svg width="9" height="9" viewBox="0 0 10 10"><path d="M1 5l3 3 5-7" stroke="#fff" stroke-width="2" fill="none"/></svg>Commercial Insurance</li>
        <li><svg width="9" height="9" viewBox="0 0 10 10"><path d="M1 5l3 3 5-7" stroke="#fff" stroke-width="2" fill="none"/></svg>Life Insurance</li>
      </ul>
      <ul class="right">
        <li><svg width="9" height="9" viewBox="0 0 10 10"><path d="M1 5l3 3 5-7" stroke="#fff" stroke-width="2" fill="none"/></svg>Health Insurance</li>
        <li><svg width="9" height="9" viewBox="0 0 10 10"><path d="M1 5l3 3 5-7" stroke="#fff" stroke-width="2" fill="none"/></svg>Farm Insurance</li>
        <li><svg width="9" height="9" viewBox="0 0 10 10"><path d="M1 5l3 3 5-7" stroke="#fff" stroke-width="2" fill="none"/></svg>Medicare Supplemental Insurance</li>
      </ul>
    </div>
  </div>
  <div class="phone">605-218-4073</div>
  <div class="web-band"><span class="web">halden-insurance.example</span></div>
</section>

</body>
</html>
```